Interior designer needs business card design

I need a card for my new interior design company. I de sign mostly kitchens and baths, but don't want the card to list and specialty. I've gotten several clients already by Dordrecht of mouth, but now need to begin advertising.
I've got a pic of a silk screen used to print my father's old real estate sign and was hoping to use it as the basis for my card design.
Instead of "Sold by Montaldo", I'd like the front of my card to read "Design by Montaldo".
I like the font styles and banner and would like to stay as close to the original as possible, but with some twist--maybe color, not sure. Surprise me!
The back should list my email and phone
montaldodesign@pellomail.com
555-271-0396

```html
<!DOCTYPE html>
<html lang="en">
<head>
<meta charset="utf-8">
<title>Design by Montaldo — Business Card</title>
<link rel="stylesheet" href="https://fonts.googleapis.com/css2?family=Jost:wght@500;600&family=Cabin:wght@400&display=swap">
<style>
  :root {
    --paper: #ffffff;
    --ink: #111111;
    --screen-red: #d9283a;
    --screen-crimson: #c81f3c;
    --screen-pink: #e2587f;
    --screen-rose: #dc3f63;
    --overlay-text: rgba(255, 255, 255, 0.32);
  }

  html, body {
    margin: 0;
    padding: 0;
    overflow: hidden;
    background: var(--paper);
  }

  .card {
    position: relative;
    width: 1200px;
    height: 704px;
    overflow: hidden;
    background: var(--paper);
  }

  .banner {
    position: absolute;
    inset: 0;
    width: 1200px;
    height: 704px;
  }

  .banner-title {
    font-family: "Jost", "Futura", sans-serif;
    font-weight: 600;
    font-size: 110px;
    fill: var(--overlay-text);
  }

  .contact {
    position: absolute;
    left: 800px;
    width: 400px;
    text-align: center;
    color: var(--ink);
    margin: 0;
    line-height: 1;
  }

  .contact-name {
    top: 534px;
    font-family: "Jost", "Futura", sans-serif;
    font-weight: 600;
    font-size: 27px;
    letter-spacing: 1.6px;
  }

  .contact-email,
  .contact-phone {
    font-family: "Cabin", "Gill Sans", sans-serif;
    font-weight: 400;
    font-size: 26px;
  }

  .contact-email { top: 592px; }
  .contact-phone { top: 644px; }

  .contact a {
    color: inherit;
    text-decoration: none;
  }
</style>
</head>
<body>
  <main class="card">
    <svg class="banner" viewBox="0 0 1200 704" xmlns="http://www.w3.org/2000/svg">
      <defs>
        <linearGradient id="screen-print" x1="0" y1="0" x2="1" y2="0.4">
          <stop offset="0" stop-color="var(--screen-rose)"/>
          <stop offset="0.3" stop-color="var(--screen-pink)"/>
          <stop offset="0.6" stop-color="var(--screen-red)"/>
          <stop offset="1" stop-color="var(--screen-crimson)"/>
        </linearGradient>
        <clipPath id="banner-shape">
          <rect x="0" y="32" width="1200" height="56"/>
          <polygon points="0,102 1200,102 1200,178 980,178 980,354 794,354 794,420 0,420"/>
          <rect x="980" y="286" width="220" height="11"/>
          <rect x="0" y="440" width="1200" height="60"/>
        </clipPath>
      </defs>

      <g role="img" aria-label="Silk-screen print of the name Montaldo in red and pink ink, cut into banner strips">
        <rect class="banner-print" x="0" y="0" width="1200" height="704" fill="url(#screen-print)" clip-path="url(#banner-shape)"/>
      </g>

      <text class="banner-title" x="-6" y="178" textLength="1212" lengthAdjust="spacingAndGlyphs">DESIGN BY MONTALDO</text>
    </svg>

    <p class="contact contact-name">DESIGN BY MONTALDO</p>
    <p class="contact contact-email"><a href="mailto:montaldodesign@pellomail.com">montaldodesign@pellomail.com</a></p>
    <p class="contact contact-phone">555-271-0396</p>
  </main>
</body>
</html>
```